Email Signature

We would like to have an email Signature designed.
We have an idea, and a logo that we would like to be make more professional in design and look.

```html
<!DOCTYPE html>
<html lang="en">
<head>
<meta charset="utf-8">
<title>Email Signature – Sam Delaney, Kestrow Consulting</title>
<link rel="stylesheet" href="https://fonts.googleapis.com/css2?family=Arimo:wght@400;700&display=swap">
<style>
  :root {
    --brand-blue: #0873b9;
    --accent-orange: #f0522a;
    --ink: #111111;
    --paper: #ffffff;
    --frame: #1a1a1a;
  }
  html, body {
    margin: 0;
    padding: 0;
    width: 1200px;
    height: 454px;
    overflow: hidden;
    background: var(--paper);
  }
  .signature {
    position: relative;
    width: 1200px;
    height: 454px;
    font-family: "Arimo", Arial, sans-serif;
    color: var(--ink);
  }
  .signature__art {
    position: absolute;
    inset: 0;
    width: 1200px;
    height: 454px;
  }
  .brand-mark {
    position: absolute;
    font-weight: 700;
    line-height: 1;
    margin: 0;
  }
  .brand-mark--panel {
    left: 62px;
    top: 160px;
    width: 290px;
    text-align: center;
    color: var(--paper);
  }
  .brand-mark--panel .brand-mark__name { font-size: 46px; letter-spacing: 2px; display: block; }
  .brand-mark--panel .brand-mark__tag { font-size: 30px; letter-spacing: 3px; display: block; margin-top: 6px; }
  .brand-mark--corner {
    right: 86px;
    top: 72px;
    text-align right;
    text-align: right;
    color: var(--brand-blue);
  }
  .brand-mark--corner .brand-mark__name { font-size: 29px; letter-spacing: 1px; display: block; }
  .brand-mark--corner .brand-mark__tag { font-size: 19px; letter-spacing: 2px; display: block; margin-top: 4px; }

  .person { position: absolute; left: 464px; top: 72px; }
  .person__name { margin: 0; font-size: 35px; font-weight: 700; line-height: 1; letter-spacing: -0.5px; }
  .person__role { margin: 4px 0 0; font-size: 16px; line-height: 1.1; }

  .contact {
    position: absolute;
    margin: 0;
    font-size: 16px;
    line-height: 22px;
    font-style: normal;
  }
  .contact--direct { left: 463px; top: 202px; }
  .contact--location { left: 466px; top: 319px; }
  .contact p { margin: 0; }
</style>
</head>
<body>
<div class="signature">
  <svg class="signature__art" viewBox="0 0 1500 567" aria-hidden="true">
    <defs>
      <clipPath id="card-area">
        <rect x="53" y="45" width="1381" height="476"/>
      </clipPath>
    </defs>
    <rect x="53" y="45" width="1381" height="476" fill="#ffffff"/>
    <g clip-path="url(#card-area)" fill="var(--brand-blue)">
      <path class="panel-disc" d="M53 45 L322 45 C470 100 580 300 443 493 L53 493 Z"/>
      <path class="panel-crescent" d="M336 45 L400 45 C500 110 580 280 505 445 C560 280 480 110 336 45 Z"/>
      <rect class="footer-band" x="53" y="493" width="1381" height="28"/>
    </g>
    <line class="divider" x1="514" y1="181" x2="1434" y2="181" stroke="var(--accent-orange)" stroke-width="2.5"/>
    <rect x="53" y="45" width="1381" height="476" fill="none" stroke="var(--frame)" stroke-width="1.5"/>

    <g class="social-links" font-family="Arimo, Arial, sans-serif" font-weight="700" font-size="12" fill="var(--brand-blue)" text-anchor="middle">
      <circle cx="162" cy="432" r="23" fill="#ffffff"/>
      <path d="M152 421 l6 -2 l4 8 l-4 3 c2 5 5 8 10 10 l3 -4 l8 4 l-2 6 c-14 1 -27 -12 -25 -25 Z" fill="var(--brand-blue)"/>
      <circle cx="228" cy="432" r="23" fill="#ffffff"/>
      <text x="228" y="436">Wubo</text>
      <circle cx="293" cy="432" r="23" fill="#ffffff"/>
      <text x="293" y="436">Fenq</text>
      <circle cx="358" cy="432" r="23" fill="#ffffff"/>
      <text x="358" y="436">Zirk</text>
    </g>
  </svg>

  <p class="brand-mark brand-mark--panel">
    <span class="brand-mark__name">KESTROW</span>
    <span class="brand-mark__tag">consulting</span>
  </p>

  <p class="brand-mark brand-mark--corner">
    <span class="brand-mark__name">KESTROW</span>
    <span class="brand-mark__tag">consulting</span>
  </p>

  <div class="person">
    <h1 class="person__name">Sam Delaney</h1>
    <p class="person__role">Client Relations</p>
  </div>

  <address class="contact contact--direct">
    <p>Mobile: +61400 555 019</p>
    <p>Emaill: abc@mailpost.com</p>
  </address>

  <address class="contact contact--location">
    <p>add : 123-xxx ,contry</p>
    <p>www.websitename.com</p>
  </address>
</div>
</body>
</html>
```